High-end residential home builder needs a business card design

We need a new business card design for a small residential construction company based in Boise, Idaho. We specialize in building custom high-end homes and remodels, with a focus on great design and craftsmanship.

We would like to use our current logo, but open to new color suggestions.
Just looking for a clean, sharp, modern design that looks high-end.

Target Market(s)

Upscale clientele

Industry/Entity Type

Contractor

Contact Information for Business Card

Company: Stonefield Custom Builders
Name: Marcus Tilley
Phone number: 208 367 4120
Email: MarcusTilleySCB@mailbox-example.com
Website: Stonefieldcustombuilders-example.com

Font styles to use
Serif
Sans Serif

Requirements
Must have
• Company Logo
Company name
My name
My phone number
My email
Company website
Nice to have
• I have attached a few photos of cards that I really like.

```html
<!DOCTYPE html>
<html lang="en">
<head>
<meta charset="utf-8">
<title>Stonefield Custom Builders – Business Card</title>
<link href="https://fonts.googleapis.com/css2?family=Montserrat:wght@500&family=Roboto:wght@400;500;700;900&display=swap" rel="stylesheet">
<style>
  :root {
    --canvas-bg: #e4e2df;
    --card-white: #f7f6f3;
    --ink-brown: #3b2616;
    --accent-orange: #d28a2c;
    --back-top: #3d2918;
    --back-bottom: #1e140b;
    --gold: #d9b55a;
  }
  * { box-sizing: border-box; margin: 0; padding: 0; }
  html, body { width: 1200px; height: 900px; overflow: hidden; }
  body {
    background: var(--canvas-bg);
    display: flex;
    align-items: center;
    justify-content: center;
    gap: 80px;
    font-family: "Roboto", sans-serif;
  }
  .card {
    width: 400px;
    height: 700px;
    border-radius: 30px;
    box-shadow: 0 18px 40px rgba(0,0,0,0.22);
    display: flex;
    flex-direction: column;
    align-items: center;
  }
  .card-front { background: var(--card-white); color: var(--ink-brown); padding-top: 110px; }
  .card-back {
    background: radial-gradient(circle at 50% 35%, var(--back-top), var(--back-bottom) 75%);
    justify-content: center;
  }
  .brand { display: flex; flex-direction: column; align-items: center; gap: 26px; }
  .brand-mark { width: 64px; height: 64px; border: 3px solid currentColor; }
  .brand-name {
    font-family: "Montserrat", sans-serif;
    font-weight: 500;
    font-size: 19px;
    letter-spacing: 0.28em;
    text-transform: uppercase;
    text-align: center;
    line-height: 1.7;
  }
  .card-front .brand { color: var(--ink-brown); }
  .card-back .brand { color: var(--gold); margin-top: -60px; }
  .person { margin-top: 62px; text-align: center; }
  .person-name { font-weight: 900; font-size: 30px; letter-spacing: 0.01em; }
  .person-title { color: var(--accent-orange); font-size: 24px; margin-top: 2px; }
  .contact-icons { display: flex; gap: 26px; margin-top: 28px; }
  .contact-icons svg { width: 30px; height: 30px; }
  .contact-list { list-style: none; text-align: center; margin-top: 26px; font-weight: 500; font-size: 18px; line-height: 1.9; }
  .bottom-rule { width: 62px; height: 3px; background: var(--ink-brown); margin-top: 40px; }
</style>
</head>
<body>
  <section class="card card-front">
    <div class="brand">
      <span class="brand-mark"></span>
      <p class="brand-name">Stonefield<br>Custom Builders</p>
    </div>
    <div class="person">
      <h1 class="person-name">MARCUS TILLEY</h1>
      <p class="person-title">Owner and Operator</p>
    </div>
    <div class="contact-icons">
      <svg viewBox="0 0 30 30" aria-label="Phone"><circle cx="15" cy="15" r="15" fill="var(--ink-brown)"/><path d="M9 12c0-2 2-3 6-3s6 1 6 3l-2 1-1-2h-6l-1 2zM10 20l2-5h6l2 5z" fill="#fff"/></svg>
      <svg viewBox="0 0 30 30" aria-label="Email"><circle cx="15" cy="15" r="15" fill="var(--ink-brown)"/><rect x="8" y="10" width="14" height="10" fill="none" stroke="#fff" stroke-width="1.5"/><path d="M8 10l7 6 7-6" fill="none" stroke="#fff" stroke-width="1.5"/></svg>
      <svg viewBox="0 0 30 30" aria-label="Website"><circle cx="15" cy="15" r="15" fill="var(--ink-brown)"/><path d="M13 17l4-4M12 14l-2 2a2.5 2.5 0 0 0 4 4l2-2M18 16l2-2a2.5 2.5 0 0 0-4-4l-2 2" fill="none" stroke="#fff" stroke-width="1.6" stroke-linecap="round"/></svg>
    </div>
    <ul class="contact-list">
      <li>(208) 367-4120</li>
      <li>MarcusTilleySCB@mailbox-example.com</li>
      <li>Stonefieldcustombuilders-example.com</li>
    </ul>
    <span class="bottom-rule"></span>
  </section>

  <section class="card card-back">
    <div class="brand">
      <span class="brand-mark"></span>
      <p class="brand-name">Stonefield<br>Custom Builders</p>
    </div>
  </section>
</body>
</html>
```